High-End Medical Center Website Design Project

This design is part of a well thought-out project by an experienced project manager / developer. The approved wireframe is attached. Creative interpretations / suggestions based on the layout encouraged.

The design is for a new state-of-the-art medical center located in Dallas, Texas. The target audience would likely be individuals (approx. 60% female /40% male) who are the healthcare decision-makers for their families. They would likely have insurance and be inclined to seek out top-quality care.

Potential clients would choose this client over others in their industry because the medical center is physician owned, meaning it is patient-focused rather than profit-focused. The facility is brand new, featuring the latest technology. (This includes an amazing waiting room featuring WiFi and docking stations.) The physicians are hand-picked by referral only.

The look of the site should be extremely clean. We are going for a well-organized, professional look with a bit of a warm glow (interpret that however you like). Use crisp corners and the colors in the logo.

Think modern, clean with some great use of color / font.

We can get lovely photography of the medical center once construction is complete. Feel free to use an "example image" behind the Featured Area ("Physician Owned. Patient-Focused") if you like. We are open to ideas.

ONE CHANGE REQUESTED IN THE WIREFRAME:

Remove the "Connect" 1/4 page footer area and replace with a quick contact form. You may swap the "Locations" area with the form if desired. Put social media icons at the top left of the page in the top header area.

(Note: Please use social media icons that match the design rather than standard icons. We preferred not placing the icons at the top, but the client requested this. Let's not bring more attention to them than necessary.)
Updates

We're custom programming this site, so there's no need to base it on a template. Also, we would prefer not to use typical "seen everywhere" stock images.Thanks.

Industry/Entity Type

Construction

Requirements
Must have
• Follow the wireframe. This has been approved.
Nice to have
• Examples of what hover states, links or dropdowns might look like.

```html
<!DOCTYPE html>
<html lang="en">
<head>
<meta charset="utf-8">
<title>Nova Medical Center</title>
<link href="https://fonts.googleapis.com/css2?family=Roboto:wght@300;400;700&display=swap" rel="stylesheet">
<style>
  :root{
    --blue:#1d5fae;
    --teal:#27a3c7;
    --orange:#f15a24;
    --ink:#333;
    --muted:#666;
    --grey:#dcdcdc;
    --grey-light:#ececec;
    --white:#fff;
  }
  *{box-sizing:border-box;margin:0;padding:0}
  html,body{width:841px;height:1200px;overflow:hidden;background:var(--white)}
  body{font-family:"Roboto",Arial,sans-serif;color:var(--ink);position:relative}
  .abs{position:absolute}

  /* header */
  .topbar{top:12px;right:30px;display:flex;align-items:center;gap:6px;font-size:12px;color:var(--muted)}
  .topbar strong{color:var(--ink);margin-right:8px}
  .social{width:18px;height:18px;border-radius:50%;background:#8a8a8a}
  .brand{top:58px;left:34px;display:flex;align-items:center;gap:8px}
  .brand-mark{width:26px;height:26px;background:var(--blue)}
  .brand-name{font-weight:700;font-size:22px;color:var(--blue);letter-spacing:.5px}
  .nav{top:78px;right:30px;display:flex;gap:22px;font-size:14px;color:var(--muted)}
  .nav a{color:inherit;text-decoration:none}
  .nav a:hover{color:var(--orange)}

  /* hero */
  .hero{top:122px;left:0;width:841px;height:312px;background:linear-gradient(90deg,#f4f7fa 0%,#e3ebf2 45%,#c9d8e6 100%)}
  .hero-title{top:158px;left:34px;font-size:26px;font-weight:300;color:var(--orange)}
  .hero-icons{top:196px;left:34px;display:flex;gap:12px}
  .hero-icons span{width:44px;height:44px;border-radius:50%;background:var(--orange);display:flex;align-items:center;justify-content:center;color:var(--white);font-size:24px;font-weight:700}

  /* features */
  .apart{top:440px;left:34px;width:152px;height:258px;background:var(--grey);padding:14px 12px}
  .apart h2{font-weight:300;font-size:40px;line-height:1.08;color:#444}
  .apart-btn{position:absolute;left:12px;bottom:14px;width:44px;height:44px;background:var(--orange);display:flex;align-items:center;justify-content:center}
  .feature{top:440px;width:198px}
  .feature-head{height:72px;background:var(--grey-light);display:flex;align-items:center;justify-content:center;text-align:center;font-size:18px;font-weight:300;text-transform:uppercase;color:#444;line-height:1.1}
  .feature-photo{height:96px}
  .feature p{font-size:10.5px;line-height:1.35;color:var(--muted);padding:8px 4px 0}

  /* promo band */
  .panel{top:722px;height:204px;display:flex;padding:16px 14px;gap:14px;color:var(--white)}
  .panel-blue{left:20px;width:402px;background:var(--blue)}
  .panel-teal{left:422px;width:399px;background:var(--teal)}
  .panel-photo{width:150px;flex:none}
  .panel h3{font-size:20px;font-weight:700;text-transform:uppercase;margin-bottom:6px}
  .panel p{font-size:10.5px;line-height:1.35}
  .btn{display:inline-block;margin-top:12px;background:var(--orange);color:var(--white);font-size:10px;font-weight:700;padding:8px 12px;text-decoration:none}

  /* footer */
  .col{top:968px;width:180px}
  .col h4{font-size:12px;font-weight:700;text-transform:uppercase;margin-bottom:8px}
  .col p{font-size:9.5px;line-height:1.3;color:var(--muted);margin-bottom:8px}
  .loc{display:flex;gap:6px}
  .wait{top:944px;left:630px;width:182px;height:176px;background:var(--grey);text-align:center;padding-top:12px}
  .wait h4{font-size:17px;font-weight:300;color:#444;margin-bottom:10px}
  .wait-box{width:90px;height:90px;margin:0 auto;background:var(--orange);color:var(--white);display:flex;flex-direction:column;align-items:center;justify-content:center}
  .wait-box b{font-size:48px;font-weight:300;line-height:1}
  .wait-box span{font-size:14px}
  .bottombar{top:1144px;left:20px;width:801px;height:26px;background:var(--grey-light);display:flex;justify-content:space-between;align-items:center;padding:0 14px;font-size:9.5px;color:var(--muted)}
</style>
</head>
<body>
  <header>
    <div class="abs topbar"><strong>Call now: (555) 014-2290</strong>
      <i class="social"></i><i class="social"></i><i class="social"></i><i class="social"></i><i class="social"></i>
    </div>
    <div class="abs brand"><span class="brand-mark"></span><span class="brand-name">NOVA MEDICAL CENTER</span></div>
    <nav class="abs nav">
      <a href="#">Why Nova</a><a href="#">Physicians</a><a href="#">Specialties</a><a href="#">Info</a><a href="#">Locations</a><a href="#">Contact</a>
    </nav>
  </header>

  <section class="abs hero" role="img" aria-label="Smiling physician in a white coat with his medical team behind him"></section>
  <h1 class="abs hero-title">Physician Owned. <strong style="font-weight:400">Patient Focused.</strong></h1>
  <div class="abs hero-icons">
    <span><svg width="22" height="22" viewBox="0 0 22 22"><path d="M8 2h6v6h6v6h-6v6H8v-6H2V8h6z" fill="#fff"/></svg></span>
    <span><svg width="24" height="18" viewBox="0 0 24 18"><rect x="1" y="1" width="22" height="16" fill="none" stroke="#fff" stroke-width="2"/><path d="M1 1l11 9 11-9" fill="none" stroke="#fff" stroke-width="2"/></svg></span>
    <span>?</span>
  </div>

  <section>
    <div class="abs apart">
      <h2>What sets us apart...</h2>
      <a class="apart-btn" href="#"><svg width="20" height="16" viewBox="0 0 20 16"><path d="M2 2l6 6-6 6M10 2l6 6-6 6" fill="none" stroke="#fff" stroke-width="2.5"/></svg></a>
    </div>
    <article class="abs feature" style="left:196px">
      <div class="feature-head">Technology</div>
      <div class="feature-photo" role="img" aria-label="Modern operating room equipment" style="background:linear-gradient(#9fb3c2,#5f7483)"></div>
      <p>Sed ut perspiciatis, unde omnis iste natus error sit voluptatem accusantium doloremque laudantium, totam rem aperiam eaque ipsa quae ab illo inventore veritatis.</p>
    </article>
    <article class="abs feature" style="left:405px">
      <div class="feature-head">Quality<br>of care</div>
      <div class="feature-photo" role="img" aria-label="Care team giving a thumbs up" style="background:linear-gradient(#c7d3dc,#7d8f9c)"></div>
      <p>Sed ut perspiciatis, unde omnis iste natus error sit voluptatem accusantium doloremque laudantium, totam rem aperiam eaque ipsa quae ab illo inventore veritatis.</p>
    </article>
    <article class="abs feature" style="left:614px">
      <div class="feature-head">Patient<br>experience</div>
      <div class="feature-photo" role="img" aria-label="Doctor talking with a senior patient" style="background:linear-gradient(#d8cfc6,#8e8279)"></div>
      <p>Sed ut perspiciatis, unde omnis iste natus error sit voluptatem accusantium doloremque laudantium, totam rem aperiam eaque ipsa quae ab illo inventore veritatis.</p>
    </article>
  </section>

  <section>
    <div class="abs panel panel-blue">
      <div class="panel-photo" role="img" aria-label="Glass facade of the medical center building" style="background:linear-gradient(#8fc3e8,#3d7fb8)"></div>
      <div>
        <h3>Corporis susci</h3>
        <p>At vero eos et accusamus et iusto odio dignissimos ducimus, qui blanditiis praesentium voluptatum deleniti atque corrupti, quos dolores et quas molestias excepturi sint, obcaecati cupi.</p>
        <a class="btn" href="#">Read More</a>
      </div>
    </div>
    <div class="abs panel panel-teal">
      <div class="panel-photo" role="img" aria-label="Smiling patient portrait" style="background:linear-gradient(#e9ddd2,#b79f8c)"></div>
      <div>
        <h3>Testimonials</h3>
        <p>At vero eos et accusamus et iusto odio dignissimos ducimus, qui blanditiis praesentium voluptatum deleniti atque corrupti, quos dolores et quas molestias excepturi sint, obcaecati cupi.</p>
        <a class="btn" href="#">Read More</a>
      </div>
    </div>
  </section>

  <footer>
    <div class="abs col" style="left:34px">
      <h4>News</h4>
      <p>Sed ut perspiciatis, unde omnis iste natus error sit.</p>
      <p>Quasi ab illo inventore veritatis et quasi architecto beatae vitae dicta sunt.</p>
      <p>Sed ut perspiciatis, unde omnis iste natus error sit.</p>
    </div>
    <div class="abs col" style="left:234px">
      <h4>Blog</h4>
      <p>Sed ut perspiciatis, unde omnis iste natus error sit.</p>
      <p>Quasi ab illo inventore veritatis et quasi architecto beatae vitae dicta sunt.</p>
      <p>Sed ut perspiciatis, unde omnis iste natus error sit.</p>
    </div>
    <div class="abs col" style="left:436px">
      <h4>Locations</h4>
      <p class="loc"><svg width="9" height="12" viewBox="0 0 9 12"><path d="M4.5 0A4.5 4.5 0 0 0 0 4.5C0 8 4.5 12 4.5 12S9 8 9 4.5A4.5 4.5 0 0 0 4.5 0z" fill="#333"/></svg>Sed ut perspiciatis, unde omnis iste natus.</p>
      <p class="loc"><svg width="9" height="12" viewBox="0 0 9 12"><path d="M4.5 0A4.5 4.5 0 0 0 0 4.5C0 8 4.5 12 4.5 12S9 8 9 4.5A4.5 4.5 0 0 0 4.5 0z" fill="#333"/></svg>Sed ut perspiciatis, unde omnis iste natus.</p>
      <p class="loc"><svg width="9" height="12" viewBox="0 0 9 12"><path d="M4.5 0A4.5 4.5 0 0 0 0 4.5C0 8 4.5 12 4.5 12S9 8 9 4.5A4.5 4.5 0 0 0 4.5 0z" fill="#333"/></svg>Sed ut perspiciatis, unde omnis iste natus.</p>
    </div>
    <div class="abs wait">
      <h4>Average Wait Time</h4>
      <div class="wait-box"><b>9</b><span>minutes</span></div>
    </div>
    <div class="abs bottombar"><span>© 2013 Nova Medical Center. All rights reserved.</span><span>Sitemap &nbsp;|&nbsp; Privacy</span></div>
  </footer>
</body>
</html>
```